Amber Hollow Cafe Business Card

We need a business card design for a new European Cafe. Main menu will be coffee and deserts.

Industry/Entity Type

Business

Requirements
Must have
• Logo - 1 of the attached versions
Address - TBA (you can use 123 Fake St Unit 1 for now)
Phone - TBA (you can use 555-555-5555 for now)

```html
<!DOCTYPE html>
<html lang="en">
<head>
<meta charset="utf-8">
<title>Amber Hollow Cafe – Business Card</title>
<link rel="stylesheet" href="https://fonts.googleapis.com/css2?family=Open+Sans:wght@400;700&family=Tinos:wght@400;700&display=swap">
<style>
  :root {
    --bg: #1e1c1b;
    --espresso: #2b221e;
    --espresso-line: #3a2f29;
    --latte: #7e6b57;
    --latte-light: #9a8570;
    --ink: #241b17;
  }
  * { box-sizing: border-box; margin: 0; padding: 0; }
  html, body { width: 1200px; height: 900px; overflow: hidden; }
  body {
    background: var(--bg);
    position: relative;
    font-family: "Open Sans", Arial, sans-serif;
  }
  .card {
    position: absolute;
    left: 300px;
    width: 600px;
    height: 340px;
    overflow: hidden;
    box-shadow: 0 12px 30px rgba(0,0,0,.45);
  }
  .card--front { top: 80px; background: var(--espresso); }
  .card--back  { top: 470px; background: var(--latte); }

  .lattice-fill {
    position: absolute;
    background: linear-gradient(135deg, var(--espresso), #30261f 50%, var(--espresso));
  }
  .card--front .lattice-fill { inset: 0; }
  .card--back .lattice-fill { left: 0; right: 0; bottom: 0; height: 64px; }

  .front-brand {
    position: absolute;
    left: 0; right: 0; top: 96px;
    display: flex; flex-direction: column; align-items: center; gap: 16px;
  }
  .brand-square {
    width: 72px; height: 72px;
    border-radius: 8px;
    background: var(--latte);
  }
  .brand-name {
    font-weight: 400;
    color: var(--latte);
    font-size: 34px;
    letter-spacing: .5px;
    white-space: nowrap;
  }

  .back-brand {
    position: absolute;
    left: 40px; top: 52px;
    display: flex; align-items: center; gap: 12px;
  }
  .back-brand .brand-square { width: 52px; height: 52px; border-radius: 6px; background: var(--ink); }
  .back-brand .brand-name { color: var(--ink); font-size: 24px; }

  .contact {
    position: absolute;
    left: 40px; top: 150px;
    font-family: "Tinos", "Times New Roman", serif;
    color: var(--ink);
  }
  .address { font-size: 17px; line-height: 1.1; font-weight: 700; }
  .phone {
    display: inline-block;
    margin-top: 6px;
    padding: 0 12px;
    background: var(--ink);
    color: var(--latte-light);
    border-radius: 6px;
    font-size: 30px;
    line-height: 38px;
    letter-spacing: 1px;
  }
  .email { margin-top: 8px; font-size: 17px; font-weight: 700; }
</style>
</head>
<body>
  <section class="card card--front">
    <div class="lattice-fill" role="img" aria-label="Diamond lattice pattern with small dots on dark brown"></div>
    <div class="front-brand">
      <div class="brand-square"></div>
      <div class="brand-name">Amber Hollow Cafe</div>
    </div>
  </section>

  <section class="card card--back">
    <div class="back-brand">
      <div class="brand-square"></div>
      <div class="brand-name">Amber Hollow Cafe</div>
    </div>
    <div class="contact">
      <p class="address">48 Linden Row, Unit 2<br>Marlow Bay CA 12345 HARWICK</p>
      <p class="phone">555.014.2270</p>
      <p class="email">info@amberhollow.com.au</p>
    </div>
    <div class="lattice-fill" role="img" aria-label="Dark brown band with diamond lattice pattern"></div>
  </section>
</body>
</html>
```